New menu design for small coffee shop

I need to design a new menu for a small cafe called The Kettle Wren. I've attached pictures of the old menu to give an idea, I really want a completely new look though. You'll notice that the food, coffee and drinks are currently on separate menus, I want all of this to be on one menu. We want to add images of the food before we print the menu, so ideally you will leave spaces for images of the food.
I'm open to suggestions on paper size and how its folded etc.
I've also attached a word file which has changes for the new menu; some are pricing updates, some are completely different.
Our Facebook page is https://www.facepage.example/thekettlewren/ might give you an idea of what we're about.
Any other questions let me know.
Cafe

```html
<!DOCTYPE html>
<html lang="en">
<head>
<meta charset="utf-8">
<title>The Kettle Wren – Trifold Menu</title>
<link rel="stylesheet" href="https://fonts.googleapis.com/css2?family=Kaushan+Script&family=Lato:wght@400;700;900&display=swap">
<style>
:root{
  --bg:#e4e5e7;
  --wood-dark:#4a2a16;
  --wood:#6b3f22;
  --wood-light:#8a5631;
  --yellow:#f7e600;
  --yellow-deep:#f1d400;
  --orange:#d9541e;
  --ink:#5b1e12;
  --ink-soft:#6e3a22;
  --paper:#ffffff;
  --grey:#e2e2e2;
  --black:#0b0b0b;
}
*{box-sizing:border-box;margin:0;padding:0}
html,body{width:1200px;height:871px;overflow:hidden}
body{background:var(--bg);font-family:"Lato",sans-serif;color:var(--ink)}
.trifold{position:absolute;left:30px;top:25px;width:1140px;height:821px;display:flex;box-shadow:0 10px 30px rgba(0,0,0,.18)}
.panel{position:relative;width:380px;height:100%;overflow:hidden;background:var(--paper)}
.wood{background:linear-gradient(180deg,var(--wood-light),var(--wood) 45%,var(--wood-dark))}
.script{font-family:"Kaushan Script",cursive}

/* menu panel */
.menu-top{height:38px}
.menu-head{height:96px;background:var(--yellow);position:relative}
.menu-title{position:absolute;left:0;right:0;top:14px;text-align:center;font-size:34px;color:var(--ink)}
.menu-ribbon{position:absolute;left:118px;top:58px;width:144px;height:30px;background:var(--orange);color:#fff;font-weight:900;font-size:20px;letter-spacing:1px;text-align:center;line-height:30px;clip-path:polygon(0 0,100% 0,94% 50%,100% 100%,0 100%,6% 50%)}
.menu-list{list-style:none;padding:22px 24px 0 26px}
.menu-item{display:flex;gap:10px;padding:9px 0;border-bottom:1px solid #b9a79b;font-size:13px;line-height:1.25;font-weight:700;color:var(--ink)}
.menu-item::before{content:"";flex:none;width:6px;height:6px;border-radius:50%;background:var(--orange);margin-top:5px}
.menu-item .desc{flex:1}
.menu-item .price{font-weight:900;font-size:15px}
.menu-gap{position:absolute;left:0;right:0;top:648px;height:26px}
.menu-feature{position:absolute;left:0;right:0;top:674px;height:130px;background:var(--yellow);padding:16px 26px;font-size:16px;line-height:1.35;color:var(--ink);text-align:center}
.menu-feature strong{font-size:22px;font-weight:900}
.menu-bottom{position:absolute;left:0;right:0;bottom:0;height:17px}

/* middle panel */
.hero{height:330px;background:radial-gradient(circle at 50% 40%,#3a2a20,var(--black) 70%)}
.badge{position:absolute;border-radius:50%;background:var(--yellow);display:flex;align-items:center;justify-content:center;text-align:center;font-family:"Lato",sans-serif;font-weight:900;color:var(--black);border:4px solid #fff}
.hero .badge{left:130px;top:110px;width:120px;height:120px;font-size:17px;line-height:1.15}
.contact{position:absolute;left:0;right:0;top:330px;height:340px;background:linear-gradient(180deg,#fff,var(--grey));text-align:center}
.rise{font-size:44px;color:#2a1a12;margin-top:26px}
.address{font-size:13px;font-weight:700;color:var(--ink);margin-top:6px;padding-bottom:8px;border-bottom:1px solid var(--ink);display:inline-block}
.phone{font-size:21px;font-weight:700;color:var(--ink);margin-top:6px}
.enjoy{font-size:19px;color:#1c1c1c;margin-top:10px}
.photos{position:absolute;left:18px;right:18px;top:206px;height:112px;background:var(--yellow);display:flex;gap:6px;padding:6px}
.photo{flex:1}
.ph-coffee{background:linear-gradient(135deg,#6f9a2c,#b5875a)}
.ph-breakfast{background:linear-gradient(135deg,#8a3a2a,#e5c86a)}
.ph-dessert{background:linear-gradient(135deg,#3b3b3b,#f0a42a)}
.foot{position:absolute;left:0;right:0;bottom:0;height:151px;display:flex;align-items:center;justify-content:center;color:#fff;font-size:18px;letter-spacing:5px;font-weight:700}
.foot::before{content:"";position:absolute;left:0;right:0;top:12px;border-top:1px solid rgba(255,255,255,.6)}

/* right panel */
.r-top{height:34px}
.r-yellow{position:absolute;left:0;right:0;top:34px;height:310px;background:linear-gradient(180deg,var(--yellow),var(--yellow-deep))}
.shake-ring{position:absolute;left:70px;top:60px;width:240px;height:200px;border-radius:50%;border:3px solid #fff;padding:8px}
.shake{width:100%;height:100%;border-radius:50%;background:radial-gradient(circle at 50% 40%,#f2e6cc,#8a5a33 75%)}
.r-yellow .badge{left:205px;top:225px;width:150px;height:130px;font-size:19px;line-height:1.15;z-index:2}
.r-grey{position:absolute;left:0;right:0;top:344px;height:326px;background:linear-gradient(180deg,#fff,var(--grey));text-align:center}
.come{font-size:30px;color:#2a1a12;margin-top:90px;line-height:1.15}
.treat{font-size:40px;color:var(--ink);line-height:1.1}
.new{font-size:19px;color:#2a1a12;margin-top:6px}
</style>
</head>
<body>
<main class="trifold">

  <section class="panel menu-panel">
    <div class="menu-top wood"></div>
    <header class="menu-head">
      <h1 class="menu-title script">All Day Breakfast Menu</h1>
      <div class="menu-ribbon">MENU</div>
    </header>
    <ul class="menu-list">
      <li class="menu-item"><span class="desc">Eggs on Turkish toast</span><span class="price">$8.0</span></li>
      <li class="menu-item"><span class="desc">Bacon and Eggs on Turkish Toast with grilled Tomato</span><span class="price">$15.0</span></li>
      <li class="menu-item"><span class="desc">Eggs Benedict - poached eggs with bacon, ham or smoked salmon and wilted baby spinach and finished with Hollandaise Sauce</span><span class="price">$18.0</span></li>
      <li class="menu-item"><span class="desc">Veggie Brekki - Our own special smashed avocado on grilled Portobello mushroom, with poached eggs, danish feta and baby Spinach.</span><span class="price">$16.0</span></li>
      <li class="menu-item"><span class="desc">High protein overnight oats - Our own protein enriched Greek yoghurt, oats and honey, topped with sliced banana</span><span class="price">$15.0</span></li>
      <li class="menu-item"><span class="desc">Omelette of the day - served with toasted Turkish bread and grilled tomato</span><span class="price">$18.0</span></li>
      <li class="menu-item"><span class="desc">Waffles - freshly toasted Waffles, maple syrup, strawberries and banana with ice cream or Cream</span><span class="price">$15.0</span></li>
      <li class="menu-item"><span class="desc">Fruit Toast</span><span class="price">$6.0</span></li>
      <li class="menu-item"><span class="desc">multigrain or White Toast with butter</span><span class="price">$4.0</span></li>
    </ul>
    <div class="menu-gap wood"></div>
    <div class="menu-feature">Wren breakfast - grilled smokey bacon, eggs, thick pork sausage, grilled mushroom topped with a lightly spiced tomato chutney, grilled tomato, lamb cutlet and hash brown with Turkish bread. <strong>$21.0</strong></div>
    <div class="menu-bottom wood"></div>
  </section>

  <section class="panel middle-panel">
    <div class="hero" role="img" aria-label="Dark photo of pastries and coffee">
      <div class="badge">The Kettle<br>Wren</div>
    </div>
    <div class="contact">
      <h2 class="rise script">Rise and shine!</h2>
      <p class="address">12/48 Harbour Lane 4410 Fernvale</p>
      <p class="phone">call us now; +617 5550 1947</p>
      <p class="enjoy script">Enjoy with our delicious coffee and dishes</p>
      <div class="photos">
        <div class="photo ph-coffee" role="img" aria-label="Photo of a latte with latte art"></div>
        <div class="photo ph-breakfast" role="img" aria-label="Photo of a cooked breakfast plate"></div>
        <div class="photo ph-dessert" role="img" aria-label="Photo of a waffle dessert"></div>
      </div>
    </div>
    <footer class="foot wood">www.kettlewren.example</footer>
  </section>

  <section class="panel cover-panel">
    <div class="r-top wood"></div>
    <div class="r-yellow">
      <div class="shake-ring"><div class="shake" role="img" aria-label="Photo of a loaded milkshake topped with banana and chocolate"></div></div>
      <div class="badge">The Kettle<br>Wren</div>
    </div>
    <div class="r-grey">
      <p class="come script">Come down<br>&amp;</p>
      <p class="treat script">Treat yourself to</p>
      <p class="new">our new loaded milkshake</p>
    </div>
    <footer class="foot wood">www.kettlewren.example</footer>
  </section>

</main>
</body>
</html>
```